Looking for a modern website banner design

Corvella Fieldmark Consultants looking for the development of the main banner of the website. The project description and photos are included in the upload files.

```html
<!DOCTYPE html>
<html lang="en">
<head>
<meta charset="utf-8">
<title>Corvella Fieldmark Consultants — Athlete Testimonial Banner</title>
<link rel="stylesheet" href="https://fonts.googleapis.com/css2?family=Libre+Caslon+Text&family=Bebas+Neue&family=Outfit:wght@400&display=swap">
<style>
  :root {
    --sky-deep: #3f5f86;
    --sky-mid: #5d7793;
    --sky-pale: #8094a6;
    --band: #25292f;
    --quote-grey: #8b9097;
    --accent-blue: #3b80c2;
    --caption-white: #ffffff;
    --photo-dark: #1c2431;
    --photo-light: #8fb7cf;
  }
  html, body {
    margin: 0;
    padding: 0;
    overflow: hidden;
    background: #ffffff;
  }
  .banner {
    position: relative;
    width: 1200px;
    height: 562px;
    overflow: hidden;
    background:
      linear-gradient(180deg,
        var(--sky-deep) 0%,
        var(--sky-pale) 4%,
        var(--sky-mid) 8%,
        var(--sky-pale) 13%,
        var(--sky-deep) 20%,
        var(--sky-mid) 40%,
        var(--sky-mid) 75%,
        var(--sky-pale) 82%,
        var(--sky-deep) 88%,
        var(--sky-pale) 93%,
        var(--sky-deep) 100%);
  }
  .brush-band {
    position: absolute;
    left: 0;
    top: 0;
    width: 1200px;
    height: 562px;
  }
  .athlete-photo {
    position: absolute;
    left: 790px;
    top: 0;
    width: 410px;
    height: 562px;
    background:
      radial-gradient(ellipse 40% 30% at 62% 45%, #6f98b3 0%, transparent 70%),
      radial-gradient(ellipse 35% 40% at 70% 78%, #2c3a4d 0%, transparent 75%),
      linear-gradient(160deg, var(--photo-light) 0%, #4f6e86 35%, var(--photo-dark) 70%, #2a3a4c 100%);
    -webkit-mask-image: linear-gradient(90deg, transparent 0%, #000 22%);
    mask-image: linear-gradient(90deg, transparent 0%, #000 22%);
  }
  .testimonial {
    position: absolute;
    left: 58px;
    top: 172px;
    width: 760px;
    margin: 0;
  }
  .quote-mark {
    position: absolute;
    font-family: "Libre Caslon Text", Georgia, serif;
    color: var(--quote-grey);
    font-size: 62px;
    line-height: 1;
  }
  .quote-mark--open { left: 0; top: -2px; }
  .quote-body {
    margin: 0 0 0 38px;
    font-family: "Libre Caslon Text", Georgia, serif;
    font-size: 19.6px;
    line-height: 34px;
    letter-spacing: -0.5px;
    color: var(--quote-grey);
    padding-top: 16px;
  }
  .program-name {
    color: var(--accent-blue);
    font-size: 31px;
    letter-spacing: -0.3px;
  }
  .program-name sup {
    font-size: 12px;
    vertical-align: 14px;
  }
  .quote-mark--close {
    position: relative;
    font-size: 48px;
    line-height: 0;
    vertical-align: -14px;
    margin-left: 3px;
  }
  .attribution {
    position: absolute;
    left: 147px;
    top: 330px;
  }
  .attribution__name {
    margin: 0;
    font-family: "Bebas Neue", "Arial Narrow", sans-serif;
    font-size: 27px;
    line-height: 1;
    color: var(--accent-blue);
    font-weight: 400;
  }
  .attribution__detail {
    margin: 5px 0 0;
    font-family: "Outfit", Arial, sans-serif;
    font-size: 12.4px;
    line-height: 19px;
    letter-spacing: 0.4px;
    color: var(--caption-white);
  }
</style>
</head>
<body>
  <section class="banner" aria-label="Athlete testimonial for Corvella Fieldmark Consultants">
    <svg class="brush-band" viewBox="0 0 1200 562" aria-hidden="true">
      <path fill="#25292f" d="M0 150 L40 135 L120 128 L200 118 L260 104 L330 92 L410 85 L480 80 L560 78 L640 70 L700 68 L760 72 L820 80 L860 90 L860 470 L820 476 L760 440 L700 432 L640 438 L600 428 L560 440 L520 444 L480 452 L420 458 L360 456 L300 466 L240 462 L200 468 L170 480 L120 486 L80 492 L40 488 L0 500 Z"/>
    </svg>

    <div class="athlete-photo" role="img" aria-label="Photograph of a smiling hockey player in team jersey and helmet, holding a stick and waving to fans, in blue duotone"></div>

    <blockquote class="testimonial">
      <span class="quote-mark quote-mark--open" aria-hidden="true">&ldquo;</span>
      <p class="quote-body">Corvella has provided support that has allowed me to develop as a person and an athlete. The <span class="program-name">A.I.M.S.<sup>TM</sup></span> process allowed me to stay focused on attainable goals each season and progress from Junior to College and now Professional Hockey.<span class="quote-mark quote-mark--close" aria-hidden="true">&rdquo;</span></p>
    </blockquote>

    <div class="attribution">
      <h2 class="attribution__name">Mason Trevell</h2>
      <p class="attribution__detail">Riverton Gales<br>Atlantic Shore Hockey League</p>
    </div>
  </section>
</body>
</html>
```